Upscale business cards needed for family office

We would like professional business cards created for employees of our family office. Relatively simple and straightforward, but also with a unique element to set them apart. Probably stick with neutral and simple colors that mesh well with the colors in the logo. We need space for the traditional elements, including name, title, address, email/phone number.

Industry/Entity Type

Business

Contact Information for Business Card

Space for name, title, phone number, email, address

```html
<!DOCTYPE html>
<html lang="en">
<head>
<meta charset="utf-8">
<title>M&amp;T Business Card</title>
<link href="https://fonts.googleapis.com/css2?family=Arimo:wght@400&display=swap" rel="stylesheet">
<style>
  :root {
    --page-bg: #e9ebec;
    --card-white: #ffffff;
    --card-grey: #e6e7e8;
    --text-grey: #7b8287;
    --title-blue: #1ba2c9;
    --band-blue: #4f7fc0;
    --band-cyan: #1fb1cf;
    --back-top: #14b7d2;
    --back-bottom: #0b95b4;
    --mark-grey: #8a9095;
  }
  * { margin: 0; padding: 0; box-sizing: border-box; }
  html, body { width: 1200px; height: 1023px; overflow: hidden; }
  body {
    background: var(--page-bg);
    font-family: "Arimo", Arial, sans-serif;
    position: relative;
  }
  .card {
    position: absolute;
    left: 250px;
    width: 700px;
    height: 400px;
    border-radius: 22px;
    overflow: hidden;
    box-shadow: 0 6px 18px rgba(0,0,0,0.18);
  }
  .card-front {
    top: 86px;
    background: radial-gradient(ellipse at 60% 35%, var(--card-white) 0%, var(--card-white) 45%, var(--card-grey) 100%);
  }
  .card-back {
    top: 537px;
    background: radial-gradient(ellipse at 50% 40%, var(--back-top) 0%, var(--back-bottom) 100%);
  }
  .front-bands { position: absolute; left: 0; top: 0; width: 700px; height: 400px; }
  .brand {
    position: absolute;
    display: flex;
    align-items: center;
    gap: 12px;
  }
  .brand-front { right: 64px; top: 44px; }
  .brand-name {
    font-size: 46px;
    color: var(--mark-grey);
    letter-spacing: 1px;
    line-height: 1;
  }
  .brand-square {
    width: 34px; height: 34px;
    background: var(--band-cyan);
  }
  .contact {
    position: absolute;
    right: 64px;
    top: 124px;
    text-align: right;
    font-size: 15px;
    line-height: 21px;
    color: var(--text-grey);
    letter-spacing: 0.8px;
  }
  .contact-line { display: flex; justify-content: flex-end; align-items: center; gap: 8px; }
  .contact-line svg { width: 13px; height: 13px; }
  .person {
    position: absolute;
    left: 60px;
    top: 228px;
  }
  .person-name {
    font-size: 28px;
    color: var(--text-grey);
    letter-spacing: 1.5px;
  }
  .person-title {
    font-size: 15px;
    color: var(--title-blue);
    letter-spacing: 0.8px;
    margin-top: 2px;
  }
  .brand-back {
    left: 50%; top: 50%;
    transform: translate(-50%, -50%);
    gap: 16px;
  }
  .brand-back .brand-name { color: var(--card-white); font-size: 64px; }
  .brand-back .brand-square { background: var(--card-white); width: 46px; height: 46px; }
</style>
</head>
<body>
  <section class="card card-front">
    <svg class="front-bands" viewBox="0 0 700 400" aria-hidden="true">
      <path d="M0 330 C 180 360 430 340 700 230 L700 246 C 440 352 200 372 0 346 Z" fill="var(--band-blue)"/>
      <path d="M0 360 C 210 392 460 372 700 262 L700 312 C 470 400 230 410 60 400 L0 400 Z" fill="var(--band-cyan)"/>
    </svg>
    <div class="brand brand-front">
      <span class="brand-square"></span>
      <span class="brand-name">M&amp;T</span>
    </div>
    <div class="contact">
      <div class="contact-line">Your address line1</div>
      <div class="contact-line">Your address line 2</div>
      <div class="contact-line">88-123-54321
        <svg viewBox="0 0 14 14"><circle cx="7" cy="7" r="6" fill="none" stroke="var(--title-blue)" stroke-width="1.4"/><path d="M5 4.5 L6 4.5 L6.6 6 L6 6.6 Q7 8 7.6 8.2 L8.2 7.6 L9.6 8.2 L9.6 9.2 Q6.5 9.8 4.6 5.6 Z" fill="var(--title-blue)"/></svg>
      </div>
      <div class="contact-line">info@yourweb.com
        <svg viewBox="0 0 14 14"><rect x="1" y="3" width="12" height="8" fill="none" stroke="var(--title-blue)" stroke-width="1.3"/><path d="M1 3 L7 8 L13 3" fill="none" stroke="var(--title-blue)" stroke-width="1.3"/></svg>
      </div>
    </div>
    <div class="person">
      <div class="person-name">Your Name</div>
      <div class="person-title">Title</div>
    </div>
  </section>

  <section class="card card-back">
    <div class="brand brand-back">
      <span class="brand-square"></span>
      <span class="brand-name">M&amp;T</span>
    </div>
  </section>
</body>
</html>
```